Best Seller Cover Design for Inspirational Non-Fiction, Self-Help Book

I've been working diligently on a book title "Quiet Harbor Rising" that will be pivotal for my coaching business. We're heavily investing in marketing and public relations for this and would love it to be a best seller (every other's dream). I need an amazing book cover design that is eye-catching, description, creative, interesting, and compelling, Can you work your magic?I've attached a detailed description along with the content for the back cover. Please let me know if all the content does not fit and I'm happy to reduce it. I need a cover that sells and speaks to the description, whatever you think that will be best. Book DetailsTitle: Self-Defined SuccessSubtitle: Spoiler Alert: You Already Have Everything It TakesAuthor: Ngan H. NguyenSpecifics:- The book will be 5.5" by 8.5" and 216 pages (may change slightly and we can update the spine in final revisions). - Paperback and leave space for a bar code- Will need the raw files so this can be redesigned into hardcover down the line- Brindlemark book cover upload ready- Final file will also need the front cover only for e-book version- Add profile headshot (attached) to back-cover if space permits.I do not have a clear vision of what will be best for this cover but I really like the evocative style of Walter Okonjo Overflowing book. Thank you!

Target Market(s)

Professionals in transition, aspiring or new entrepreneurs, change-makers.

Font styles to use
Serif
Script

Colors

Designer to choose colors to be used in the design.

Requirements
Must have
• Traditional but with elements that make it interesting and provocative since it is speaking to a twist on a topic that has been well talked about, success.

```html
<!DOCTYPE html>
<html lang="en">
<head>
<meta charset="utf-8">
<title>Quiet Harbor Rising — Book Cover</title>
<link rel="stylesheet" href="https://fonts.googleapis.com/css2?family=Arimo:wght@400;700&family=Tinos:wght@400&display=swap">
<style>
  :root {
    --stage: #555555;
    --paper: #ffffff;
    --paper-shade: #e9e9e9;
    --ink: #1a1a1a;
    --title-red: #d9141c;
    --title-blue: #0b4a8b;
    --spine-edge: #dcdcdc;
  }
  * { box-sizing: border-box; margin: 0; padding: 0; }
  html, body {
    width: 1200px; height: 800px; overflow: hidden;
    background: var(--stage);
  }
  .book-spread {
    position: absolute; left: 153px; top: 70px;
    width: 894px; height: 660px;
    display: flex;
    box-shadow: 0 10px 30px rgba(0,0,0,0.35);
  }
  /* Back cover */
  .back-cover {
    width: 427px; height: 100%;
    background: var(--paper);
    padding: 48px 38px 40px 42px;
    font-family: "Arimo", Arial, sans-serif;
    font-size: 9.2px; line-height: 1.3; color: var(--ink);
  }
  .back-cover p { margin-bottom: 11px; }
  .author-bio {
    display: flex; gap: 14px; margin-top: 18px; align-items: flex-start;
  }
  .author-bio .headshot { flex: 0 0 76px; height: 76px; display: block; }
  .author-bio p { margin: 0; }
  /* Spine */
  .spine {
    width: 40px; height: 100%;
    background: linear-gradient(90deg, #f4f4f4, var(--paper) 40%, var(--paper-shade));
    border-left: 1px solid var(--spine-edge);
    border-right: 1px solid var(--spine-edge);
    position: relative;
  }
  .spine-title, .spine-author {
    position: absolute; left: 50%;
    writing-mode: vertical-rl;
    transform: translateX(-50%);
    white-space: nowrap;
  }
  .spine-title {
    top: 46px;
    font-family: "Arimo", Arial, sans-serif; font-size: 18px;
  }
  .spine-title .red { color: var(--title-red); }
  .spine-title .blue { color: var(--title-blue); font-weight: 700; }
  .spine-author {
    bottom: 40px;
    font-family: "Tinos", "Times New Roman", serif; font-size: 15px; color: var(--ink);
  }
  /* Front cover */
  .front-cover {
    width: 427px; height: 100%;
    position: relative; overflow: hidden;
    background: linear-gradient(180deg, var(--paper) 0%, #f6f6f6 45%, #e6e6e6 100%);
  }
  .front-author {
    position: absolute; top: 62px; width: 100%; text-align: center;
    font-family: "Tinos", "Times New Roman", serif; font-size: 24px;
    letter-spacing: 0.5px; color: var(--ink);
  }
  .front-title {
    position: absolute; top: 124px; width: 100%; text-align: center;
    font-family: "Arimo", Arial, sans-serif; line-height: 1;
  }
  .front-title .line-red {
    display: block; color: var(--title-red); font-size: 40px; font-weight: 400;
  }
  .front-title .line-blue {
    display: block; color: var(--title-blue); font-size: 66px; font-weight: 700;
    letter-spacing: 6px; margin-top: 4px;
  }
  .front-subtitle {
    position: absolute; top: 268px; width: 100%; text-align: center;
    font-family: "Arimo", Arial, sans-serif; color: var(--ink);
  }
  .front-subtitle .lead { display: block; font-size: 22px; margin-bottom: 6px; }
  .front-subtitle .rest { display: block; font-size: 15px; }
  .front-artwork {
    position: absolute; left: 0; bottom: 0; width: 427px; height: 330px; display: block;
  }
</style>
</head>
<body>
  <div class="book-spread">
    <section class="back-cover">
      <p>I have come to believe that all the striving, working hard, accumulating wealth and material possessions, or pursuing new goals is an endeavor to find that sense of happiness and fulfillment. That when we finally achieve that end goal, it would allow us to wake up in peace and completeness. Feeling like we've finally made it and now life is a joy.</p>
      <p>The precious time and life energy we pour into these endeavors are non-refundable, and it is essential that the end destination is one that will bring that ultimate satisfaction. Following someone else's path or society's definition of success may not ultimately bring that sense of fulfillment. It has to be your dream and not someone else's. That in the end, success is at what we each genuinely want for our lives and not only what is defined by others because what will bring that sense of completeness is internal fulfillment and not external accolades.</p>
      <p>You can achieve anything you desire, but success in any endeavor depends on your passion for the pursuit. Passion is what ignites the heart, fires the soul, and fills the spirit. It is passion that energizes and sparks the pull forward through all barriers, uncertainty, and challenges.</p>
      <p>It is the love for our dreams that enlivens our being and furnishes the energy for us to move unyieldingly forward. For this journey, we are asked to turn inward to search for the invisible, the hidden, and the sacred possibilities for our lives to claim what is ours in truth. Then fuel it with a desire that will ignite its creation. It needs to be a possible future that fuels us with a burning desire that transcends all real and imagined barriers. Only genuine desire and deep love, evoked from the deepest recesses of the heart, maintain such a passion.</p>
      <p>May this book serve as your guide on how to evoke this clarity and desire for your dreams. Enabling you to create a vision for your future vision that will be a worthwhile end destination and ultimate sense of fulfillment. In addition, showing you the steps on how to navigate the path forward towards this new dream. Enabling you to develop innate faculties you each already possess.</p>
      <p>My dream is that this book serves the purposes to be a companion on your path to your most authentic and extraordinary success.</p>
      <div class="author-bio">
        <svg class="headshot" role="img" aria-label="Author headshot photograph" viewBox="0 0 76 76">
          <defs>
            <linearGradient id="headshotTone" x1="0" y1="0" x2="1" y2="1">
              <stop offset="0" stop-color="#3a4a5a"/>
              <stop offset="1" stop-color="#7a5a44"/>
            </linearGradient>
          </defs>
          <rect width="76" height="76" fill="url(#headshotTone)"/>
        </svg>
        <p>Tove R. Lindqvar has built her platform of a vision-driven life after 10 years of experience working as a business strategy advisor in Meridian 500 companies and at Halvorsen &amp; Reed. Helping business leaders solve their most pressing challenges to achieve their vision. Combining her experience as a business strategy advisor with her passion for self-development, spirituality, and self-actualization, she now works as an Intuitive Strategist - empowering entrepreneurs, change-makers, and leaders to step into their truth and bring their unique vision to life. Enabling them to change their lives, revolutionize their work, create greater impact in the world.</p>
      </div>
    </section>

    <section class="spine">
      <div class="spine-title"><span class="red">QUIET HARBOR </span><span class="blue">RISING</span></div>
      <div class="spine-author">TOVE R. LINDQVAR</div>
    </section>

    <section class="front-cover">
      <div class="front-author">TOVE R. LINDQVAR</div>
      <h1 class="front-title">
        <span class="line-red">QUIET HARBOR</span>
        <span class="line-blue">RISING</span>
      </h1>
      <div class="front-subtitle">
        <span class="lead">Fair Warning:</span>
        <span class="rest">The Map Was Folded In Your Pocket</span>
      </div>
      <svg class="front-artwork" role="img" aria-label="Black and white chess pieces on a checkered board, black king facing white pieces" viewBox="0 0 427 330">
        <defs>
          <linearGradient id="chessTone" x1="1" y1="0" x2="0" y2="1">
            <stop offset="0" stop-color="#f2f2f2" stop-opacity="0"/>
            <stop offset="0.35" stop-color="#c8c8c8"/>
            <stop offset="0.75" stop-color="#555555"/>
            <stop offset="1" stop-color="#111111"/>
          </linearGradient>
        </defs>
        <rect width="427" height="330" fill="url(#chessTone)"/>
      </svg>
    </section>
  </div>
</body>
</html>
```